Quorvane Consulting

We focus on Data Recovery but we also do Network Security. We recover data from all types of hard drive form factors 3.5", 2.5", 1", 1.8", 5.25", 8" with any kind of interface IDE(PATA), SATA, mSATA, SCSI, SAS and Fibre Channel. All RAID Arrays 0, 1, 2, 3, 4, 5, 10 including nested levels like RAID 0+1, 1+0, 100, 0+3, 50 and 60, flash drives, like tablets, cellphones, usb drives, memory cards(SD, miniSD, Memory Stick(hovaku))

Actually you can gather any information or text from any data recovery site, cause is usually the same info, we would probably change a couple of things from the description so it wont look the same. One thing though, we want to make clear to users not to attempt data recovery themselves and to ship the faulty device to us, maybe we can illustrate this?

the Data Recovery link can have sub menus like "Data Recovery Process - Data Recovery Services - F.A.Q"

the Penetration Testing can have sub menus like "F.A.Q - Pentest Process - Pentest Services"

Here are links from website so you gather information:

-http://www.brelwick-disks.example/

-http://www.tolvenpathrescue.example/

-http://www.nimbrocore.example/

http://fentaloprestore.example/lp/disk-restore.aspx?src=web&ref=ZQPLx4TrmvaKDJ-wuHafk9RB2x
http://www.vqlt.example/
http://www.pembrastoneflow.example/data-recovery/
http://www.ytsarchiverescue.example/

thanks.

Target Market(s)

Any PC user

Industry/Entity Type

Data Recovery

Requirements
Must have
• - Language and geographic navigation
- Home page navigation
- Global navigation
- Breadcrumbs
Nice to have
• - Sliders
-Drop down navigation

```html
<!DOCTYPE html>
<html lang="en">
<head>
<meta charset="utf-8">
<title>Quorvane Consulting — Data Recovery</title>
<link rel="stylesheet" href="https://fonts.googleapis.com/css2?family=Open+Sans:wght@400;600;700&family=Roboto:wght@400;500;700&display=swap">
<style>
:root{
  --red:#d10f14;
  --red-dark:#b0070c;
  --red-deep:#8e0a0d;
  --charcoal:#3c3c3c;
  --charcoal-dark:#333;
  --ink:#3d3d3d;
  --muted:#8a8a8a;
  --rule:#d9d9d9;
  --white:#fff;
  --page-bg:#eeeeee;
  --link:#1aa3d8;
}
*{box-sizing:border-box;margin:0;padding:0}
html,body{width:1141px;height:1200px;overflow:hidden}
body{background:var(--page-bg);font-family:"Open Sans",sans-serif;color:var(--ink);position:relative}
.page{position:absolute;left:114px;top:0;width:912px;height:1200px;background:var(--white)}
.abs{position:absolute}

/* header */
.masthead{left:0;top:0;width:912px;height:146px;background:linear-gradient(180deg,#c60f14 0%,#d81a1f 45%,#c10d12 100%)}
.utility-bar{left:0;top:0;width:912px;height:25px;background:linear-gradient(180deg,#a40a0e,#b80c11)}
.utility-bar .promo{left:27px;top:4px;font:700 13.5px "Open Sans",sans-serif;color:var(--white);white-space:nowrap}
.utility-bar .promo span{margin-left:8px}
.locale{left:710px;top:5px;font:700 11.5px "Open Sans",sans-serif;color:var(--white);white-space:nowrap}
.locale u{text-underline-offset:2px}
.locale .sep{margin:0 14px}
.main-nav a{position:absolute;top:100px;font:500 15px "Roboto",sans-serif;color:var(--white);text-decoration:none;white-space:nowrap}
.brand{left:376px;top:37px;width:160px;height:160px;border-radius:50%;background:var(--white);box-shadow:0 2px 6px rgba(0,0,0,.25);display:flex;align-items:center;justify-content:center;z-index:3}
.brand span{font:700 17px "Open Sans",sans-serif;color:var(--charcoal-dark);text-align:center;line-height:1.2}
.sub-nav{left:0;top:146px;width:912px;height:36px;background:var(--charcoal);border-top:1px solid #222;border-bottom:1px solid #222}
.sub-nav a{position:absolute;top:10px;font:700 11.5px "Roboto",sans-serif;color:var(--white);text-decoration:none;white-space:nowrap}

/* hero */
.hero{left:0;top:182px;width:912px;height:366px;background:linear-gradient(90deg,#c9c9c7 0%,#dcdcd9 35%,#e6e6e4 60%,#d0d3d8 100%)}
.hero-photo{left:365px;top:60px;width:547px;height:306px;background:radial-gradient(ellipse at 60% 45%,#9fb3d6 0%,#a9b9d4 30%,#d8d8d8 65%,rgba(220,220,218,0) 80%)}
.hero h1{left:30px;top:78px;font:700 38px/1 "Open Sans",sans-serif;letter-spacing:-2px;color:var(--red);white-space:nowrap}
.hero h2{left:30px;top:124px;font:600 38px/1 "Open Sans",sans-serif;letter-spacing:-2.2px;color:#555;white-space:nowrap}
.hero p{left:32px;top:177px;width:420px;font:400 13px/22px "Open Sans",sans-serif;color:var(--white)}
.btn-pill{left:32px;top:272px;width:134px;height:42px;border-radius:21px;background:linear-gradient(#fff,#e4e4e4);box-shadow:0 3px 5px rgba(0,0,0,.3);font:600 15px/42px "Open Sans",sans-serif;letter-spacing:-.5px;color:#1e1e1e;text-align:center}

/* service cards */
.card{top:562px;width:216px;height:104px;border-radius:4px;background:linear-gradient(180deg,#d90f14,#c20b10);box-shadow:0 2px 3px rgba(0,0,0,.25)}
.card h3{position:absolute;left:18px;top:15px;font:400 19.5px/21px "Roboto",sans-serif;color:var(--white)}
.card h3 b{font-weight:700}
.card .more{position:absolute;left:18px;top:72px;width:74px;height:20px;border-radius:10px;background:linear-gradient(#fff,#e6e6e6);font:400 10.5px/20px "Roboto",sans-serif;color:#333;text-align:center}
.card svg{position:absolute;top:20px}

/* content */
.section-title{font:400 19px "Roboto",sans-serif;letter-spacing:-.3px;color:#2d2d2d;white-space:nowrap}
.welcome-title{left:34px;top:708px}
.welcome-text{left:34px;top:750px;width:540px;font:400 11.4px/19px "Open Sans",sans-serif;color:var(--muted)}
.welcome-text p+p{margin-top:19px}
.services-title{left:626px;top:708px}
.services-rule{left:624px;top:745px;width:256px;height:1px;background:#cfcfcf}
.services-list{left:624px;top:759px;width:256px;list-style:none}
.services-list li{height:33.5px;border-bottom:2px solid #ececec;padding:7px 0 0 9px;font:400 12.5px "Open Sans",sans-serif;letter-spacing:.5px;color:#555}

/* footer */
.footer{left:0;top:950px;width:912px;height:250px;background:var(--charcoal)}
.footer h4{position:absolute;top:35px;font:400 19px "Roboto",sans-serif;color:var(--white);white-space:nowrap}
.footer .col{position:absolute;font:400 10.5px/16px "Open Sans",sans-serif;color:var(--white)}
.field{position:absolute;left:28px;width:176px;height:26px;border-radius:3px;background:linear-gradient(#fff,#e7e7e7);font:400 10px/26px "Open Sans",sans-serif;color:#aaa;padding-left:10px}
.forgot{position:absolute;left:34px;top:143px;font:400 10px "Open Sans",sans-serif;color:#ddd}
.btn-login{position:absolute;left:29px;top:164px;width:72px;height:23px;border-radius:3px;background:linear-gradient(#e2141a,#b20a0f);font:400 12.5px/23px "Roboto",sans-serif;color:var(--white);padding-left:14px}
.footer .author{color:var(--link)}
.sitemap{list-style:none}
.sitemap li{height:22px}
.legal{position:absolute;left:0;top:211px;width:912px;height:1px;background:#4a4a4a}
.copyright{position:absolute;left:29px;top:225px;font:400 12px "Roboto",sans-serif;color:var(--white)}
.bottom-nav{position:absolute;right:36px;top:225px;font:400 12px "Roboto",sans-serif;color:var(--white);white-space:nowrap}
.bottom-nav span{margin:0 8px}
</style>
</head>
<body>
<div class="page">

  <header>
    <div class="abs masthead"></div>
    <div class="abs utility-bar">
      <div class="abs promo">Free Consultation Service <span>OR</span> <span>555-014-2278</span></div>
      <div class="abs locale"><u>English</u><span class="sep">|</span>United States&nbsp;&nbsp;▾</div>
    </div>
    <nav class="main-nav">
      <a style="left:26px">Home</a>
      <a style="left:125px">Contact</a>
      <a style="left:238px">Penetration Test</a>
      <a style="left:557px">Data Receovery</a>
      <a style="left:723px">Careers</a>
      <a style="left:834px">About</a>
    </nav>
    <div class="abs brand"><span>Quorvane<br>Consulting</span></div>
    <nav class="abs sub-nav">
      <a style="left:27px">Data Recovery Process</a>
      <a style="left:174px">Data Recovery Services</a>
      <a style="left:325px">F.A.Q</a>
    </nav>
  </header>

  <section class="abs hero">
    <div class="abs hero-photo" role="img" aria-label="Photo of a technician in gloves inspecting an opened hard drive with a magnifying glass on a workbench with tools"></div>
    <h1 class="abs">Dont Try it yourself</h1>
    <h2 class="abs">If &nbsp;we can’t do. No one can do...</h2>
    <p class="abs">Lorem ipsum dolor sit amet, consectetuer adipiscing elit, sed diam nonummy nibh euismod tincidunt ut laoreet dolore magna aliquam erat volutpat.</p>
    <div class="abs btn-pill">READ MORE</div>
  </section>

  <section class="service-cards">
    <div class="abs card" style="left:10px">
      <h3>Hard Disk<br><b>Recovery</b></h3>
      <div class="more">Read More</div>
      <svg style="left:140px" width="48" height="64" viewBox="0 0 48 64"><rect x="1" y="1" width="46" height="62" rx="6" fill="#fff"/><circle cx="24" cy="36" r="15" fill="#c60e13"/><circle cx="24" cy="36" r="10" fill="#fff"/><circle cx="24" cy="36" r="4" fill="#c60e13"/><circle cx="7" cy="7" r="2" fill="#c60e13"/><circle cx="41" cy="7" r="2" fill="#c60e13"/><path d="M10 52 L22 40" stroke="#c60e13" stroke-width="3"/></svg>
    </div>
    <div class="abs card" style="left:235px">
      <h3>Raid<br><b>Recovery</b></h3>
      <div class="more">Read More</div>
      <svg style="left:150px" width="50" height="60" viewBox="0 0 50 60"><path d="M8 1 H42 L49 12 H1 Z" fill="#fff"/><rect x="1" y="15" width="48" height="13" fill="#fff"/><rect x="1" y="31" width="48" height="13" fill="#fff"/><rect x="1" y="47" width="48" height="12" fill="#fff"/><g fill="#c60e13"><rect x="6" y="19" width="22" height="4"/><rect x="6" y="35" width="22" height="4"/><rect x="6" y="51" width="22" height="4"/></g></svg>
    </div>
    <div class="abs card" style="left:460px">
      <h3>Flash<br><b>Drive Recovery</b></h3>
      <div class="more">Read More</div>
      <svg style="left:178px" width="24" height="60" viewBox="0 0 24 60"><rect x="4" y="1" width="16" height="14" fill="#fff"/><rect x="8" y="5" width="3" height="5" fill="#c60e13"/><rect x="13" y="5" width="3" height="5" fill="#c60e13"/><rect x="1" y="17" width="22" height="42" fill="#fff"/></svg>
    </div>
    <div class="abs card" style="left:685px">
      <h3>Network<br><b>Securities</b></h3>
      <div class="more">Read More</div>
      <svg style="left:130px" width="68" height="60" viewBox="0 0 68 60"><rect x="20" y="1" width="28" height="20" rx="3" fill="#fff"/><rect x="26" y="8" width="16" height="2.5" fill="#c60e13"/><rect x="26" y="13" width="16" height="2.5" fill="#c60e13"/><path d="M34 21 V32 M9 42 V32 H59 V42 M34 32 V42" stroke="#fff" stroke-width="3" fill="none"/><rect x="0" y="44" width="18" height="14" rx="4" fill="#fff"/><rect x="25" y="44" width="18" height="14" rx="4" fill="#fff"/><rect x="50" y="44" width="18" height="14" rx="4" fill="#fff"/></svg>
    </div>
  </section>

  <section>
    <h2 class="abs section-title welcome-title">WELCOME TO QUORVANE CONSULTING</h2>
    <div class="abs welcome-text">
      <p>Lorem ipsum dolor sit amet, consectetuer adipiscing elit, sed diam nonummy nibh euismod tinci-dunt ut laoreet dolore magna aliquam erat volutpat. Ut wisi enim ad minim veniam, quis nostrud exerci tation ullamcorper suscipit lobortis nisl ut aliquip ex ea commodo consequat. Duis autem vel eum iriure dolor in hendrerit in vulputate velit esse molestie consequat,</p>
      <p>&nbsp;vel illum dolore eu feugiat nulla facilisis at vero eros et accumsan et iusto odio dignissim qui blan-dit praesent luptatum zzril delenit augue duis dolore te feugait nulla facilisi. Nam liber tempor cum soluta nobis eleifend option congue nihil imperdiet doming id quod mazim placerat facer possim assum.</p>
    </div>
    <h2 class="abs section-title services-title">OTHER SERVICES</h2>
    <div class="abs services-rule"></div>
    <ul class="abs services-list">
      <li>Mobile Phones</li>
      <li>MP3 Players</li>
      <li>Digital Cameras</li>
      <li>Tablets</li>
    </ul>
  </section>

  <footer class="abs footer">
    <h4 style="left:31px">Member Login</h4>
    <div class="field" style="top:75px">username</div>
    <div class="field" style="top:111px">password</div>
    <div class="forgot">Forgot your password</div>
    <div class="btn-login">Log in</div>

    <h4 style="left:250px">Testimonials</h4>
    <div class="col" style="left:251px;top:72px;width:210px">
      <p>Lorem Ipsum est simplement du faux texte employé.</p>
      <p style="margin-top:16px">If you want us to design your colour chart contact us</p>
      <p class="author" style="margin-top:16px">Teodor Halvik</p>
    </div>

    <h4 style="left:508px">SiteMap</h4>
    <ul class="col sitemap" style="left:509px;top:72px">
      <li>Lorem ipsum dolosdr</li>
      <li>Consectetuer adipisc</li>
      <li>Diam nonummy nibh</li>
      <li>Cincidunt ut laoreget</li>
      <li>Dolore magna aliqua</li>
      <li>Ut wisi enim ad mini</li>
    </ul>

    <h4 style="left:709px">Contact Details</h4>
    <div class="col" style="left:709px;top:72px;width:190px">
      <p>Contact details will be appear here contact details here</p>
      <p style="margin-top:16px">Phone No. : 1-800-555-0193</p>
      <p style="margin-top:16px">E-mail : info@quorvane.example</p>
    </div>

    <div class="legal"></div>
    <div class="copyright">Copyright 2012 Website Name. All Rights Reserved.</div>
    <div class="bottom-nav">Home<span>|</span>About<span>|</span>Penetration Test<span>|</span>Data Receovery<span>|</span>Careers</div>
  </footer>

</div>
</body>
</html>
```